Smartphone App
Zielgruppe
Wir vertreiben ein Produkt (Name: Vorlix) mit dem Smartphone Apps erstellt werden können, quasi ein CMS für Smartphone Apps. Wir verkaufen dem Kunden das Produkt und dazu die Dienstleistung das Produkt beim Kunden zu installieren und zu personalisieren Analog zur Einrichtung eines CMS für eine Webseite.
Aufgabenstellung
Wir benötigen einen Flyer A4 den wir per Briefpost zur Kaltaquise versenden können.
Die Message die wir transportieren möchten ist, dass man heute mit einer Smartphone App neue Möglichkeiten hat, Informationen zum Kunden (Stammkunden) zu kommunizieren. Dass es einfach und schnell geht, eine eigene App zu haben und dass die Pflege kinderleicht ist und keine Fachkenntnisse erfordert. Schlagworte bezügl. der Funktionen der App: Informationen, Push-Nachrichten, Terminkalender, Reservierung, Verkauf, Bestellung. Der Leser soll neugierig darauf werden und einen Termin für eine unverbindliche Beratung vereinbaren. Bilder sollten Smartphone und Kundenbindung rüberbringen. Das Design sollte die Zielgruppe Gastronomen und Einzelhändler, also in der Regel Inhaber geführte Geschäfte ansprechen. Auf den Flyer sollten Informationen zu uns sein.

```html
<!DOCTYPE html>
<html lang="de">
<head>
<meta charset="utf-8">
<title>Flyer Smartphone App – Vorder- und Rückseite</title>
<link rel="stylesheet" href="https://fonts.googleapis.com/css2?family=Arimo:wght@700&family=Rubik:wght@700;800&display=swap">
<style>
  :root {
    --bg-light: #f2f2f2;
    --bg-mid: #d6d6d6;
    --bar-gray: #5b5b5b;
    --panel-gray: #6a6d69;
    --panel-gray-dark: #4f534f;
    --brand-green: #3a913d;
    --brand-green-dark: #2d7a31;
    --text-white: #ffffff;
    --text-black: #111111;
  }
  * { box-sizing: border-box; margin: 0; padding: 0; }
  html, body { width: 1200px; height: 712px; overflow: hidden; }
  body {
    position: relative;
    background: radial-gradient(ellipse at 50% 45%, var(--bg-light) 0%, var(--bg-mid) 100%);
    font-family: "Rubik", "Arial Black", sans-serif;
    color: var(--text-white);
  }
  .side-label {
    position: absolute;
    top: 38px;
    width: 416px;
    text-align: center;
    font-family: "Arimo", Arial, sans-serif;
    font-weight: 700;
    font-size: 33px;
    color: var(--text-black);
  }
  .side-label--front { left: 146px; }
  .side-label--back { left: 637px; }

  .flyer-page {
    position: absolute;
    top: 92px;
    width: 417px;
    height: 589px;
    background: var(--bar-gray);
    box-shadow: 0 10px 18px rgba(0,0,0,0.35);
    overflow: hidden;
  }
  .flyer-page--front { left: 146px; }
  .flyer-page--back { left: 637px; }

  .hero-visual {
    position: absolute;
    left: 0; top: 11px;
    width: 100%; height: 179px;
    background: radial-gradient(ellipse at 50% 55%, #cfe9d0 0%, #f4f8f4 55%, #ffffff 100%);
  }
  .photo-backdrop {
    position: absolute;
    left: 0; top: 203px;
    width: 100%; height: 292px;
    background: linear-gradient(160deg, #7b7f79 0%, var(--panel-gray) 45%, var(--panel-gray-dark) 100%);
  }
  .flyer-page--back .photo-backdrop {
    top: 11px; height: 484px;
    background: linear-gradient(165deg, #6e726d 0%, var(--panel-gray) 50%, #4a4e4a 100%);
  }

  .headline-tile {
    position: absolute;
    left: 120px; top: 220px;
    width: 164px; height: 164px;
    background: linear-gradient(180deg, #43a046 0%, var(--brand-green) 60%, var(--brand-green-dark) 100%);
    border-radius: 4px;
    box-shadow: 0 4px 8px rgba(0,0,0,0.35);
    text-align: center;
  }
  .headline-tile__lead {
    margin-top: 40px;
    font-size: 18px;
    line-height: 24px;
    font-weight: 800;
  }
  .headline-tile__app {
    font-size: 41px;
    line-height: 48px;
    font-weight: 800;
    color: #f0f0f0;
    text-shadow: 0 2px 3px rgba(0,0,0,0.45);
  }

  .benefit-list {
    position: absolute;
    left: 110px; top: 407px;
    list-style: none;
    font-size: 16.5px;
    line-height: 19px;
    font-weight: 700;
  }
  .benefit-list li::before {
    content: "";
    display: inline-block;
    width: 4px; height: 4px;
    margin-right: 5px;
    vertical-align: middle;
    background: var(--brand-green);
    border-radius: 50%;
  }

  .contact-band {
    position: absolute;
    left: 0; bottom: 0;
    width: 100%; height: 81px;
    background: var(--brand-green);
    text-align: center;
    font-size: 15.5px;
    line-height: 15.5px;
    font-weight: 700;
    padding-top: 28px;
  }
  .flyer-page--back .contact-band { padding-top: 32px; }

  .feature-title {
    position: absolute;
    left: 29px; top: 36px;
    font-size: 33px;
    font-weight: 800;
    letter-spacing: 0.5px;
    text-shadow: 0 2px 3px rgba(0,0,0,0.5);
    padding-bottom: 2px;
    border-bottom: 4px solid var(--text-white);
  }
  .feature-list {
    position: absolute;
    left: 31px; top: 95px;
    list-style: none;
    font-size: 23.5px;
    font-weight: 800;
    text-shadow: 0 2px 3px rgba(0,0,0,0.4);
  }
  .feature-list li { height: 33.5px; }
  .feature-list li.gap { margin-top: 5px; }
  .consult-note {
    position: absolute;
    left: 39px; top: 316px;
    width: 340px;
    font-size: 15.5px;
    line-height: 20px;
    font-weight: 700;
    letter-spacing: 0.3px;
  }
</style>
</head>
<body>
  <div class="side-label side-label--front">Vorderseite</div>
  <div class="side-label side-label--back">Rückseite</div>

  <section class="flyer-page flyer-page--front">
    <div class="hero-visual" role="img" aria-label="Illustration: Smartphones, Tablets, Monitor und Laptop mit grünen App-Oberflächen und Symbolen"></div>
    <div class="photo-backdrop" role="img" aria-label="Abgedunkeltes Foto: Smartphone auf einem Tisch"></div>
    <div class="headline-tile">
      <p class="headline-tile__lead">GANZ EINFACH<br>EINE EIGENE</p>
      <p class="headline-tile__app">APP!</p>
    </div>
    <ul class="benefit-list">
      <li>Neue Möglichkeiten</li>
      <li>Kinderleichte Pflege</li>
      <li>Ohne Fachkenisse</li>
    </ul>
    <footer class="contact-band">
      Netzwerkstatt-Partner Jonas Brendel<br>
      Telefon: 02345-610284<br>
      www.netzwerkstatt-partner.de
    </footer>
  </section>

  <section class="flyer-page flyer-page--back">
    <div class="photo-backdrop" role="img" aria-label="Abgedunkeltes Foto: Smartphone mit eingeblendeten App-Symbolen"></div>
    <h2 class="feature-title">Funktionen der APP</h2>
    <ul class="feature-list">
      <li>Informationen</li>
      <li>Push Narichten</li>
      <li>Terminkalender</li>
      <li>Reservierung</li>
      <li class="gap">Verkauf</li>
      <li>Bestellung</li>
    </ul>
    <p class="consult-note">Bei Interesse einfach einen Termin machen um profesionelle Beratung zu bekommen.</p>
    <footer class="contact-band">
      Netzwerkstatt-Partner Jonas Brendel<br>
      Telefon: 02345-610284<br>
      www.netzwerkstatt-partner.de
    </footer>
  </section>
</body>
</html>
```